Alarm System package Ad for Chatterbox and flyer

Looking to create a Chatterbox add & flyer (A4) for an alarm system package
It will be used in paid Chatterbox advertising and letterbox drops
Once design is decided I will require 2-3 different pricing versions but using the same layout/design

The alarm package is a very cheap deal and the system itself if most suitable for smaller homes and smaller businesses.
The package includes back to base alarm monitoring on a contract for a minimum 12 months. This is at an additional cost (terms and conditions will explain this)

Target Market(s)

families, small business owners, home owners,

Industry/Entity Type

Advertising

Font styles to use
Sans Serif

Colors

Designer to choose colors to be used in the design.

Requirements
Must have
• Harbourline Alarms logo to be easily visible
• the alarm package will be priced at $299 (and 2 other version will be required upon approval of design)
• it will need a section to state terms and conditions apply
• KWL Linked (logo)
• Image of the parts
• minimal wording eg'Fully installed monitored alarm system" then the price
Nice to have
• family and/or home in the background
• Colors similar to my logo
• Logo on the ad
Should not have
• must not have a corporate feel

```html
<!DOCTYPE html>
<html lang="en">
<head>
<meta charset="utf-8">
<title>Harbourline Alarms – Monitored Alarm System Flyer</title>
<link rel="stylesheet" href="https://fonts.googleapis.com/css2?family=Montserrat:wght@500;600;700;800;900&display=swap">
<style>
  :root {
    --navy: #17398a;
    --navy-deep: #123077;
    --sky: #5ccbf2;
    --white: #ffffff;
    --stage: #e6e7e9;
    --ink: #1b3f93;
  }
  * { box-sizing: border-box; margin: 0; padding: 0; }
  html, body {
    width: 1200px; height: 1000px; overflow: hidden;
    background: var(--stage);
    font-family: "Montserrat", Arial, sans-serif;
  }
  .canvas { position: relative; width: 1200px; height: 1000px; }
  .flyer {
    position: absolute; left: 270px; top: 33px;
    width: 660px; height: 934px;
    background: var(--white);
    box-shadow: 0 6px 24px rgba(0,0,0,.18);
    overflow: hidden;
  }
  .flyer-shapes { position: absolute; inset: 0; width: 660px; height: 934px; }

  .partner-logo {
    position: absolute; left: 150px; top: 48px;
    display: flex; align-items: center; gap: 10px;
    font-weight: 800; font-size: 30px; color: var(--ink); letter-spacing: -.5px;
  }
  .partner-logo .mark { width: 22px; height: 22px; border-radius: 50%; background: var(--sky); }

  .brand-logo {
    position: absolute; right: 36px; top: 118px;
    display: flex; align-items: center; gap: 10px;
    font-weight: 800; font-size: 22px; color: var(--ink); text-transform: uppercase; line-height: 1.05;
  }
  .brand-logo .mark { width: 34px; height: 34px; background: var(--ink); }

  .headline {
    position: absolute; left: 36px; top: 610px; width: 290px;
    text-transform: uppercase; font-weight: 900; line-height: .98;
  }
  .headline .lead { display: block; color: var(--white); font-size: 32px; font-weight: 800; }
  .headline .main { display: block; color: var(--sky); font-size: 42px; letter-spacing: -.5px; white-space: nowrap; }

  .price-badge {
    position: absolute; left: 286px; top: 540px;
    width: 118px; height: 118px; border-radius: 50%;
    background: var(--navy); border: 4px solid var(--white);
    display: flex; flex-direction: column; align-items: center; justify-content: center;
    color: var(--white);
  }
  .price-badge .amount { font-size: 34px; font-weight: 900; line-height: 1; }
  .price-badge .label { font-size: 20px; font-weight: 600; color: var(--white); line-height: 1.1; }

  .terms {
    position: absolute; left: 30px; top: 840px;
    font-size: 9px; font-weight: 700; color: var(--white); letter-spacing: .3px;
  }
</style>
</head>
<body>
<main class="canvas">
  <article class="flyer">
    <svg class="flyer-shapes" viewBox="0 0 660 934">
      <defs>
        <linearGradient id="familyPhotoTone" x1="0" y1="0" x2="0" y2="1">
          <stop offset="0" stop-color="#c9d6e2"/>
          <stop offset=".45" stop-color="#b7c4c9"/>
          <stop offset=".75" stop-color="#8fae7a"/>
          <stop offset="1" stop-color="#6f9a55"/>
        </linearGradient>
        <linearGradient id="productTone" x1="0" y1="0" x2="1" y2="1">
          <stop offset="0" stop-color="#f4f5f7"/>
          <stop offset="1" stop-color="#c9ccd2"/>
        </linearGradient>
      </defs>

      <rect class="family-photo" x="0" y="90" width="660" height="500" fill="url(#familyPhotoTone)"
            role="img" aria-label="Photo of a smiling family of four standing in front of their house"/>

      <path class="header-band" d="M0 0 H660 V200 C470 178 230 118 0 78 Z" fill="#ffffff"/>
      <path class="header-stripe" d="M0 78 C230 118 470 178 660 200 V222 C470 196 230 132 0 90 Z" fill="var(--navy)"/>

      <path class="footer-edge" d="M0 532 C160 500 320 510 450 548 C540 574 610 580 660 576 V934 H0 Z" fill="#ffffff"/>
      <path class="footer-panel" d="M0 548 C160 516 320 526 450 564 C540 590 610 596 660 592 V934 H0 Z" fill="var(--navy)"/>

      <rect class="product-photo" x="344" y="672" width="292" height="220" rx="14" fill="url(#productTone)"
            role="img" aria-label="Alarm system parts: keypad control panel, two motion sensors, door sensor and remote key fob"/>
    </svg>

    <div class="partner-logo"><span class="mark"></span>KWL Linked</div>
    <div class="brand-logo"><span class="mark"></span>Harbourline<br>Alarms</div>

    <h1 class="headline">
      <span class="lead">Fully</span>
      <span class="lead">Installed</span>
      <span class="main">Monitored</span>
      <span class="main">Alarm</span>
      <span class="main">System</span>
    </h1>

    <div class="price-badge">
      <span class="amount">$299</span>
      <span class="label">VALUE</span>
    </div>

    <p class="terms">*TERMS AND CONDITIONS APPLY</p>
  </article>
</main>
</body>
</html>
```